Market Corner Fair needs a poster design

We need a poster to promote our showcase to both potential local vendors now, and visitors to the show on the actual day. See attached files and also checkout our Chatterbook page - "Market Corner Fair" for more information. Please state that booths are 8' (don't say 8' by 8'). See attached info that we have done so far, but we need something more professional. Ensure you use the Stay Bright Buy Nearby logo. The poster should be printable on both letter (8 1/2" by 11') and ledger sizes (11" by 17"). I have attached a sample of the poster from our last event - the Dwelling Expo 2013. I want the new poster similar to this (doesn't have to be exact, this is just to give you an idea.. The grand prize this time is a trip for two! The contact info has changed too, please note it on the new poster. I am no longer with my last company (UofW, Brantmoor Campus), so don't put that on the new poster. Thank you. You can email me with any questions. marketcornerfair@mailbay.example

Target Market(s)

Vendors for booth rentals. The community to visit the show.... They need to know that someone is going to win a trip for 2. We also have food, beer and wine sampling.

Industry/Entity Type

It Company

Font styles to use
Sans Serif

Requirements
Must have
• Stay bright buy nearby logo. Location. Email. Phone numbers. "Like our Chatterbook page - "Market Corner Fair". Poster is meant to attract business vendors now and to advertise the show to the public to attend in April. Must be able to print the poster on both letter size and ledger size paper. Need it in jpg too for Chatterbook uploads
Nice to have
• If it fits would be nice to say first of its kind in North Grenville
• First annual Market Corner Fair
Should not have
• Not too wordy.... Can't be confusing. Don't really need booth size on poster. Just state that both booths and marketplace tables are available. Not too many colours. We will be putting the poster in the newspaper in black and white only!

```html
<!DOCTYPE html>
<html lang="en">
<head>
<meta charset="utf-8">
<title>Market Corner Fair – Poster Variations</title>
<link href="https://fonts.googleapis.com/css2?family=Questrial&family=Open+Sans:wght@400;700;800&family=Oswald:wght@600&display=swap" rel="stylesheet">
<style>
  :root{
    --page:#ffffff;
    --khaki:#cbc5a5;
    --taupe:#625a4a;
    --bag-light:#d2bb8f;
    --bag-dark:#b89d6e;
    --ink:#4a4a44;
    --ink-soft:#5a5950;
    --cream:#d3cbb0;
    --blue:#3b8ee0;
    --pink:#db6f80;
    --pink-pale:#f2b3bd;
    --magenta:#e3267c;
    --orange:#f39a3a;
    --yellow:#f3ec2a;
    --purple:#9a2bd6;
    --dot-blue:#4a8fd8;
    --lime:#8ae62c;
    --crimson:#dc2c62;
    --amber:#f5a230;
    --tag:#f4f1ec;
    --badge:#d8d8d4;
    --badge-dark:#3a3a38;
    --logo-green:#39a51b;
    --back-pink:#e49a9c;
    --back-green:#8fcf2a;
    --outline:#e8e4d8;
  }
  html,body{margin:0;padding:0;}
  body{
    width:1200px;height:556px;overflow:hidden;position:relative;
    background:var(--page);
    font-family:"Open Sans",Arial,sans-serif;
  }
  .poster{position:absolute;top:0;width:357px;height:556px;}
  .poster svg{display:block;width:357px;height:556px;}
  .poster--khaki{left:0;background:var(--khaki);}
  .poster--outline{left:415px;background:var(--taupe);}
  .poster--solo{left:835px;background:var(--taupe);}

  .title{font-family:"Questrial",Arial,sans-serif;font-size:29px;}
  .venue{font-family:"Open Sans",Arial,sans-serif;font-weight:700;font-size:9.5px;}
  .date{font-family:"Questrial",Arial,sans-serif;font-size:14px;}
  .hours{font-family:"Questrial",Arial,sans-serif;font-size:14px;}
  .annual{font-family:"Questrial",Arial,sans-serif;font-size:16px;}
  .edition{font-family:"Questrial",Arial,sans-serif;font-size:12px;}

  .category{font-family:"Open Sans",Arial,sans-serif;font-size:12.5px;fill:var(--ink-soft);}
  .category--big{font-size:15px;}
  .prize{font-family:"Oswald",Arial,sans-serif;font-weight:600;fill:var(--magenta);}

  .badge-label{font-family:"Open Sans",Arial,sans-serif;font-weight:800;font-size:7px;fill:var(--badge-dark);}
  .badge-label--booth{font-size:9.5px;}
  .badge-price{font-family:"Open Sans",Arial,sans-serif;font-weight:800;font-size:11px;fill:var(--badge-dark);}
  .badge-note{font-family:"Open Sans",Arial,sans-serif;font-weight:700;font-size:4.5px;fill:var(--badge-dark);}
  .info{font-family:"Open Sans",Arial,sans-serif;font-weight:700;font-size:7.5px;}
  .logo-word{font-family:"Open Sans",Arial,sans-serif;font-weight:700;font-size:6px;fill:#fff;}
</style>
</head>
<body>

<article class="poster poster--khaki">
  <svg viewBox="0 0 357 556" xmlns="http://www.w3.org/2000/svg">
    <defs>
      <linearGradient id="bag-fill" x1="0" y1="0" x2="1" y2="1">
        <stop offset="0" stop-color="var(--bag-light)"/>
        <stop offset="1" stop-color="var(--bag-dark)"/>
      </linearGradient>

      <g id="bag-contents">
        <circle cx="250" cy="185" r="18" fill="var(--purple)"/>
        <circle cx="113" cy="238" r="17" fill="var(--dot-blue)"/>
        <ellipse cx="183" cy="315" rx="33" ry="30" fill="var(--lime)"/>
        <circle cx="97" cy="383" r="21" fill="var(--crimson)"/>
        <ellipse cx="224" cy="412" rx="49" ry="41" fill="var(--amber)"/>

        <text class="category" text-anchor="middle">
          <tspan x="168" y="192">Home</tspan>
          <tspan x="168" y="205">Services,</tspan>
          <tspan x="168" y="218">Sales &amp;</tspan>
          <tspan x="166" y="231">Renovations</tspan>
        </text>
        <text class="category" text-anchor="middle">
          <tspan x="135" y="276">Local Dining</tspan>
          <tspan x="135" y="288">and</tspan>
          <tspan x="138" y="300">Confectionaries</tspan>
        </text>
        <text class="category" text-anchor="middle">
          <tspan x="130" y="338">Weddings</tspan>
          <tspan x="130" y="351">Planning/</tspan>
          <tspan x="130" y="364">Caterers/</tspan>
          <tspan x="128" y="377">Decor</tspan>
        </text>
        <text class="category category--big" text-anchor="middle">
          <tspan x="215" y="384">Artisans &amp;</tspan>
          <tspan x="215" y="398">One</tspan>
          <tspan x="215" y="412">of a Kind</tspan>
          <tspan x="215" y="426">Creations</tspan>
        </text>
        <text class="category" text-anchor="middle" transform="rotate(4 115 430)">
          <tspan x="115" y="427">Healthy Active</tspan>
          <tspan x="115" y="440">Living Services</tspan>
        </text>

        <g transform="rotate(5 243 282)">
          <rect x="215" y="226" width="56" height="114" fill="var(--tag)"/>
          <circle cx="243" cy="234" r="3" fill="var(--bag-dark)"/>
          <text class="prize" text-anchor="middle">
            <tspan x="243" y="252" font-size="11">The</tspan>
            <tspan x="243" y="264" font-size="11">grand</tspan>
            <tspan x="243" y="281" font-size="16">PRIZE</tspan>
            <tspan x="243" y="298" font-size="15">A trip</tspan>
            <tspan x="243" y="315" font-size="15">for</tspan>
            <tspan x="243" y="332" font-size="15">two!</tspan>
          </text>
        </g>
      </g>

      <g id="footer">
        <rect x="10" y="497" width="46" height="24" rx="3" fill="var(--badge)"/>
        <text class="badge-label" text-anchor="middle">
          <tspan x="33" y="505">Marketplace</tspan>
          <tspan x="33" y="512">tables</tspan>
          <tspan x="33" y="519">available</tspan>
        </text>
        <rect x="10" y="524" width="46" height="19" rx="3" fill="var(--badge)"/>
        <text class="badge-price" x="33" y="538" text-anchor="middle">$150</text>

        <rect x="62" y="497" width="44" height="24" rx="3" fill="var(--badge)"/>
        <text class="badge-label badge-label--booth" text-anchor="middle">
          <tspan x="84" y="508">Booths</tspan>
          <tspan x="84" y="518" style="font-size:7px">available</tspan>
        </text>
        <rect x="62" y="524" width="44" height="19" rx="3" fill="var(--badge)"/>
        <text class="badge-price" x="78" y="538" text-anchor="middle">$250</text>
        <text class="badge-note" text-anchor="middle">
          <tspan x="99" y="531">after</tspan>
          <tspan x="99" y="536">April 1st</tspan>
          <tspan x="99" y="541">$300</tspan>
        </text>

        <rect x="287" y="505" width="58" height="41" fill="var(--logo-green)"/>
        <text class="logo-word" text-anchor="middle">
          <tspan x="316" y="520">STAY BRIGHT</tspan>
          <tspan x="316" y="528">BUY</tspan>
          <tspan x="316" y="536">NEARBY</tspan>
        </text>
      </g>
    </defs>

    <rect x="10" y="12" width="26" height="108" fill="var(--pink)"/>
    <text class="annual" fill="var(--pink-pale)" transform="rotate(-90 28 80)" x="28" y="80">Annual</text>
    <text class="edition" fill="#fff" transform="rotate(-90 29 114)" x="29" y="114">1<tspan font-size="7" dy="-4">st</tspan></text>

    <text class="title" fill="var(--blue)"><tspan x="38" y="36">MARKET CORNER</tspan><tspan x="38" y="63">FAIR</tspan></text>
    <text class="venue" x="40" y="76" fill="var(--ink)">NORTHVALE MUNICIPAL CENTRE</text>
    <text class="date" x="40" y="91" fill="var(--ink)">SATURDAY -  APRIL 18, 2015</text>
    <text class="hours" x="40" y="106" fill="var(--pink)">9AM – 3PM</text>

    <g role="img" aria-label="Two coloured shopping bags, pink and lime, standing behind the main bag">
      <rect x="66" y="114" width="248" height="358" fill="var(--back-pink)" opacity="0.85"/>
      <rect x="92" y="120" width="253" height="350" fill="var(--back-green)" opacity="0.9"/>
    </g>
    <rect role="img" aria-label="Kraft paper shopping bag with rope handles" x="60" y="150" width="245" height="330" fill="url(#bag-fill)"/>
    <use href="#bag-contents"/>

    <use href="#footer"/>
    <text class="info" text-anchor="middle" fill="var(--ink)">
      <tspan x="195" y="514">More information available on Chatterbook</tspan>
      <tspan x="195" y="524">“Brantmoor Market Corner Fair”</tspan>
      <tspan x="195" y="537">marketcornerfair@mailbay.example</tspan>
    </text>
  </svg>
</article>

<article class="poster poster--outline">
  <svg viewBox="0 0 357 556" xmlns="http://www.w3.org/2000/svg">
    <rect x="10" y="12" width="26" height="108" fill="var(--cream)"/>
    <text class="annual" fill="var(--magenta)" transform="rotate(-90 28 80)" x="28" y="80">Annual</text>
    <text class="edition" fill="var(--magenta)" transform="rotate(-90 29 114)" x="29" y="114">1<tspan font-size="7" dy="-4">st</tspan></text>

    <text class="title" fill="var(--cream)"><tspan x="38" y="36">MARKET CORNER</tspan><tspan x="38" y="63">FAIR</tspan></text>
    <text class="venue" x="40" y="76" fill="var(--orange)">NORTHVALE MUNICIPAL CENTRE</text>
    <text class="date" x="40" y="91" fill="var(--cream)">SATURDAY -  APRIL 18, 2015</text>
    <text class="hours" x="40" y="106" fill="var(--orange)">9AM – 3PM</text>

    <rect role="img" aria-label="Outlined shopping bag standing behind the main bag" x="58" y="116" width="270" height="351" fill="var(--taupe)" stroke="var(--outline)" stroke-width="1"/>
    <rect role="img" aria-label="Kraft paper shopping bag with rope handles" x="68" y="158" width="268" height="340" fill="url(#bag-fill)"/>
    <use href="#bag-contents" transform="translate(8 3)"/>

    <use href="#footer"/>
    <text class="info" text-anchor="middle" fill="var(--cream)">
      <tspan x="195" y="514">More information available on Chatterbook</tspan>
      <tspan x="195" y="524">“Brantmoor Market Corner Fair”</tspan>
      <tspan x="195" y="537">marketcornerfair@mailbay.example</tspan>
    </text>
  </svg>
</article>

<article class="poster poster--solo">
  <svg viewBox="0 0 357 556" xmlns="http://www.w3.org/2000/svg">
    <rect x="10" y="12" width="26" height="108" fill="var(--cream)"/>
    <text class="annual" fill="var(--magenta)" transform="rotate(-90 28 80)" x="28" y="80">Annual</text>
    <text class="edition" fill="var(--magenta)" transform="rotate(-90 29 114)" x="29" y="114">1<tspan font-size="7" dy="-4">st</tspan></text>

    <text class="title" fill="var(--cream)"><tspan x="38" y="36">MARKET CORNER</tspan><tspan x="38" y="63">FAIR</tspan></text>
    <text class="venue" x="40" y="76" fill="var(--yellow)">NORTHVALE MUNICIPAL CENTRE</text>
    <text class="date" x="40" y="91" fill="var(--cream)">SATURDAY -  APRIL 18, 2015</text>
    <text class="hours" x="40" y="106" fill="var(--orange)">9AM – 3PM</text>

    <rect role="img" aria-label="Large kraft paper shopping bag with rope handles" x="42" y="114" width="268" height="382" fill="url(#bag-fill)"/>
    <use href="#bag-contents" transform="translate(-2 -8) scale(1.02)"/>

    <use href="#footer"/>
    <text class="info" text-anchor="middle" fill="var(--cream)">
      <tspan x="195" y="514">More information available on Chatterbook</tspan>
      <tspan x="195" y="524">“Brantmoor Market Corner Fair”</tspan>
      <tspan x="195" y="537">marketcornerfair@mailbay.example</tspan>
    </text>
  </svg>
</article>

</body>
</html>
```